Corporate Branding - Web and Print

A UK based company will like to use an existing logo to create branding materials for all marketing related documents, including business card, prints, letterhead, Website, Twitter, Facebook, Instagram logo etc. This company serves high-end clientele in the fashion, health and wellness and as such high quality and class is of utmost importance.
Where the logo can be modernised without losing its character then experiment. The main thing is to have a corporate branding which can be used later for brochures, Business Plan infographics.
The prominent colour within the organisation is burnt orange with no secondary colour. However if you believe a secondary colour is needed then use it, otherwise keep it simple and classy. Any chosen colours have to match perfectly.
Target Market(s)
High net worth individuals
Industry/Entity Type
Health And Wellness
Contact Information for Business Card
classy
Look and feel
Each slider illustrates characteristics of the customer's brand and the style your logo design should communicate.

```html
<!DOCTYPE html>
<html lang="en">
<head>
<meta charset="utf-8">
<title>Velmora — Business Card</title>
<link rel="stylesheet" href="https://fonts.googleapis.com/css2?family=Montserrat:wght@700;800&family=Lato:wght@400;700&display=swap">
<style>
  :root {
    --stage: #2b2b2b;
    --card: #1b1b1b;
    --card-edge: #242424;
    --orange: #f39019;
    --white: #f4f4f4;
    --rule: #6a6a6a;
    --halo: rgba(255,255,255,0.035);
  }
  * { margin: 0; padding: 0; box-sizing: border-box; }
  html, body { width: 1200px; height: 1189px; overflow: hidden; }
  body {
    background: radial-gradient(ellipse at 40% 30%, #3a3a3a 0%, var(--stage) 60%, #1c1c1c 100%);
    font-family: "Lato", sans-serif;
    position: relative;
  }
  .card {
    position: absolute;
    left: 150px;
    width: 900px;
    height: 514px;
    background: var(--card);
    border-radius: 34px;
    box-shadow: 0 18px 40px rgba(0,0,0,0.55);
    overflow: hidden;
  }
  .card--front { top: 58px; }
  .card--back { top: 617px; }

  /* front */
  .front__halo {
    position: absolute;
    width: 360px; height: 360px;
    left: 270px; top: 60px;
    border-radius: 50%;
    background: var(--halo);
  }
  .wordmark {
    font-family: "Montserrat", sans-serif;
    font-weight: 800;
    color: var(--orange);
    letter-spacing: 1px;
    line-height: 1;
    white-space: nowrap;
  }
  .front__wordmark {
    position: absolute;
    left: 0; right: 0; top: 200px;
    text-align: center;
    font-size: 92px;
  }
  .front__web {
    position: absolute;
    left: 0; right: 0; top: 318px;
    text-align: center;
    font-size: 22px;
    letter-spacing: 1.5px;
    color: var(--white);
  }
  .front__web .accent { color: var(--orange); }

  /* back */
  .back__wordmark {
    position: absolute;
    left: 60px; top: 220px;
    font-size: 68px;
  }
  .back__rule {
    position: absolute;
    left: 478px; top: 70px;
    width: 1px; height: 370px;
    background: var(--rule);
  }
  .contact {
    position: absolute;
    left: 520px; top: 100px;
    color: var(--white);
  }
  .contact__name {
    font-family: "Montserrat", sans-serif;
    font-weight: 800;
    font-size: 27px;
    line-height: 1;
    letter-spacing: 0.3px;
  }
  .contact__title {
    color: var(--orange);
    font-size: 22px;
    margin-top: 2px;
  }
  .contact__address {
    margin-top: 38px;
    font-size: 22px;
    line-height: 1.25;
  }
  .contact__list {
    list-style: none;
    margin-top: 10px;
    font-size: 22px;
  }
  .contact__item {
    display: flex;
    align-items: center;
    gap: 8px;
    height: 34px;
  }
  .contact__icon {
    width: 30px; height: 30px;
    flex: none;
  }
</style>
</head>
<body>

<section class="card card--front" aria-label="Card front">
  <div class="front__halo"></div>
  <div class="wordmark front__wordmark">VELMORA</div>
  <div class="front__web">www.<span class="accent">velmora</span>.com</div>
</section>

<section class="card card--back" aria-label="Card back">
  <div class="wordmark back__wordmark">VELMORA</div>
  <div class="back__rule"></div>
  <div class="contact">
    <div class="contact__name">DANIEL HART</div>
    <div class="contact__title">Managing Partner</div>
    <div class="contact__address">PO BOX 48 Crescent Road<br>Mayfair, London, UK</div>
    <ul class="contact__list">
      <li class="contact__item">
        <svg class="contact__icon" viewBox="0 0 30 30" aria-hidden="true">
          <circle cx="15" cy="15" r="15" fill="#f39019"/>
          <path d="M9 12c0-2 3-3 6-3s6 1 6 3v1h-3v-1.5h-6V13H9z M10 14h10l1 6H9z" fill="#1b1b1b"/>
          <circle cx="15" cy="17" r="1.8" fill="#f39019"/>
        </svg>
        (01) 4821 5530
      </li>
      <li class="contact__item">
        <svg class="contact__icon" viewBox="0 0 30 30" aria-hidden="true">
          <circle cx="15" cy="15" r="15" fill="#f39019"/>
          <rect x="8" y="10" width="14" height="10" fill="none" stroke="#1b1b1b" stroke-width="1.6"/>
          <path d="M8 10l7 6 7-6" fill="none" stroke="#1b1b1b" stroke-width="1.6"/>
        </svg>
        info@velmora.com
      </li>
      <li class="contact__item">
        <svg class="contact__icon" viewBox="0 0 30 30" aria-hidden="true">
          <circle cx="15" cy="15" r="15" fill="#f39019"/>
          <circle cx="15" cy="15" r="7" fill="none" stroke="#1b1b1b" stroke-width="1.4"/>
          <ellipse cx="15" cy="15" rx="3" ry="7" fill="none" stroke="#1b1b1b" stroke-width="1.2"/>
          <path d="M8 15h14M9.5 11.5h11M9.5 18.5h11" stroke="#1b1b1b" stroke-width="1.1"/>
        </svg>
        www.velmora.com
      </li>
    </ul>
  </div>
</section>

</body>
</html>
```